Website for legal expungement services with button to qualify/disqualify potential clients

Brightfield Record Relief, LLC is a law firm focusing in legal expungement servcies (allowing people to erase criminal court records, police records, proseution files, etc). I want a more modern look which exudes confidence in the services. I am looking for a clean website that looks very polished. I want to keep the pages to a minimum, as I want the page not so much to answer questions, but to direct traffic to contact the law office. I would like the main focus point to be an button which would take a client through a series of questions to see if they would qualify for the services; this serves two purposes 1) to collect contact info for future marketing via email and 2) eliminate individuals who we are currently unable to help. A current theme that I have played around with are "Change so much, you'll need to reintroduce yourself" alongside a picture of a guys hand outstretched.
On the landing page, I would like a very brief and to the point explanation of what the service would be (i.e. "Leave your past in the past; expunge all your criminal records" ), followed by a list of benefits that it provides. (NB: included is a file "law post card-02" that includes the main benefits to expungement). Also included are two logo files for a more updated logo I currently use ("BRR Logo" and BRR Logo2") (NB: I'm open to revisions on this as well). Lastly, I've had two very minor 'ads' that I did ("postcard back" and "HVU Ad") that I like the idea of.

Target Market(s)

Middle/upper-middle class, mostly male, people with a criminal record or criminal accusation

Industry/Entity Type

Legal Services

Coding

Coded - Design and coding required

Requirements
Must have
• Button that attracts attention up front (possibly stand out coloring) to click to open up a series of questions to qualify/eliminate prospects, and simultaneously gather their info. Also, must be mobile friendly.

```html
<!DOCTYPE html>
<html lang="en">
<head>
<meta charset="utf-8">
<title>Brightfield Record Relief</title>
<link rel="stylesheet" href="https://fonts.googleapis.com/css2?family=Cinzel:wght@400;500;600&family=Poppins:wght@400;500;600&display=swap">
<style>
:root{
  --navy:#073a78;
  --blue:#0b4b96;
  --deep:#062f63;
  --ink:#1f2a3a;
  --white:#ffffff;
}
*{box-sizing:border-box;margin:0;padding:0}
html,body{width:1200px;height:3447px;overflow:hidden}
body{position:relative;background:var(--white);font-family:"Poppins",sans-serif;color:var(--ink)}
h1,h2{font-weight:400}
.abs{position:absolute}
.btn{position:absolute;display:flex;align-items:center;justify-content:center;background:var(--blue);color:var(--white);font-family:"Poppins",sans-serif;font-weight:600;font-size:14px;text-decoration:none}
.img-fill{position:absolute}

/* hero */
.hero{position:absolute;left:0;top:0;width:1200px;height:519px;
  background:
    radial-gradient(ellipse 190px 300px at 830px 330px,rgba(22,36,70,.95) 0%,rgba(28,44,82,.85) 45%,rgba(28,44,82,0) 100%),
    radial-gradient(ellipse 120px 110px at 820px 110px,rgba(140,110,90,.55) 0%,rgba(140,110,90,0) 100%),
    linear-gradient(100deg,#9aa2ab 0%,#b8bec5 45%,#a4abb4 100%)}
.brand{position:absolute;left:161px;top:38px;display:flex;align-items:center;gap:14px}
.brand-mark{width:22px;height:22px;background:var(--navy)}
.brand-name{font-family:"Cinzel",serif;font-weight:600;font-size:17px;line-height:19px;color:var(--navy);letter-spacing:.5px}
.hero-title{position:absolute;left:158px;top:146px;font-family:"Cinzel",serif;font-weight:500;font-size:46px;line-height:54px;color:var(--white);letter-spacing:.5px}
.hero-title .lead{color:var(--navy)}
.hero-photo{left:680px;top:20px;width:400px;height:499px}

/* services */
.section-title{position:absolute;font-family:"Cinzel",serif;font-weight:500;font-size:40px;color:var(--navy);letter-spacing:1px}
.scales-bg{left:860px;top:880px;width:340px;height:260px;background:radial-gradient(ellipse at 60% 60%,rgba(214,190,150,.35),rgba(255,255,255,0) 70%)}
.svc-photo{width:388px;height:257px}
.svc-one{left:161px;top:685px;background:
  radial-gradient(ellipse 120px 70px at 300px 190px,rgba(40,30,25,.8),rgba(40,30,25,0)),
  radial-gradient(ellipse 170px 110px at 150px 130px,#e9e7e3 0%,rgba(233,231,227,.3) 70%,rgba(233,231,227,0)),
  linear-gradient(135deg,#5a4330 0%,#9a7a55 40%,#2f3f66 100%)}
.svc-two{left:623px;top:685px;background:
  radial-gradient(ellipse 150px 90px at 260px 200px,#efe9e2 0%,rgba(239,233,226,0) 100%),
  radial-gradient(ellipse 110px 70px at 120px 50px,#2c3552 0%,rgba(44,53,82,0) 100%),
  linear-gradient(135deg,#3a2a22 0%,#7a5433 45%,#b58c63 70%,#d9d2c8 100%)}
.svc-icon{position:absolute;width:71px;height:70px;background:var(--blue);display:flex;align-items:center;justify-content:center}
.svc-label{position:absolute;height:59px;background:var(--white);border:1.5px solid var(--navy);display:flex;align-items:center;padding-left:14px;font-family:"Cinzel",serif;font-weight:500;font-size:15px;color:var(--ink);letter-spacing:1px}
.svc-arrow{position:absolute;width:30px;height:59px;background:var(--navy);display:flex;align-items:center;justify-content:center}

/* about */
.about-photo{left:0;top:1058px;width:579px;height:412px;background:
  radial-gradient(ellipse 70px 200px at 50px 260px,#8e9096 0%,rgba(142,144,150,0) 100%),
  radial-gradient(ellipse 80px 220px at 170px 270px,#2c3550 0%,rgba(44,53,80,0) 100%),
  radial-gradient(ellipse 70px 230px at 300px 270px,#1f3564 0%,rgba(31,53,100,0) 100%),
  radial-gradient(ellipse 70px 220px at 400px 260px,#23314f 0%,rgba(35,49,79,0) 100%),
  radial-gradient(ellipse 60px 210px at 520px 270px,#4e4e52 0%,rgba(78,78,82,0) 100%),
  linear-gradient(90deg,#6e7074 0%,#51606e 35%,#7f8a8c 60%,#a07d58 80%,#6b4e36 100%)}
.about-band{left:579px;top:1140px;width:621px;height:107px;background:var(--blue)}
.about-panel{left:579px;top:1247px;width:621px;height:223px;background:var(--navy)}
.about-strip{left:161px;top:1470px;width:1039px;height:90px;background:var(--navy)}
.panel-title{position:absolute;font-family:"Cinzel",serif;font-weight:500;font-size:40px;color:var(--white);letter-spacing:1px}
.about-text{left:626px;top:1276px;width:420px;font-size:13.5px;line-height:24.5px;color:var(--white)}
.about-text p+p{margin-top:8px}

/* benefits */
.benefits-bg{left:0;top:1560px;width:1200px;height:715px;background:
  radial-gradient(ellipse 260px 200px at 280px 560px,rgba(190,200,215,.55),rgba(190,200,215,0)),
  radial-gradient(ellipse 220px 180px at 560px 580px,rgba(200,208,220,.5),rgba(200,208,220,0)),
  linear-gradient(180deg,#ffffff 0%,#f4f6f9 45%,#e9edf2 100%)}
.benefits-bar{left:1113px;top:1560px;width:87px;height:543px;background:var(--blue)}
.benefits-intro{left:163px;top:1704px;width:880px;font-size:14px;line-height:24.5px;color:var(--ink)}
.benefit{position:absolute;display:flex;align-items:center;gap:20px}
.benefit-icon{width:60px;height:60px;border:1.5px solid var(--blue);background:var(--white);display:flex;align-items:center;justify-content:center}
.benefit-text{font-size:14px;line-height:24.5px;color:var(--ink)}

/* records */
.records-photo{left:621px;top:2194px;width:579px;height:517px;background:
  radial-gradient(ellipse 200px 70px at 420px 40px,#1f2226 0%,rgba(31,34,38,0) 100%),
  radial-gradient(ellipse 160px 40px at 360px 150px,#5c5f66 0%,rgba(92,95,102,0) 100%),
  radial-gradient(ellipse 120px 110px at 40px 480px,#c9a98c 0%,rgba(201,169,140,0) 100%),
  linear-gradient(160deg,#3a3d43 0%,#aeb4bd 22%,#e7eaef 45%,#d5dae2 70%,#c4c9d2 100%)}
.records-band{left:0;top:2276px;width:621px;height:173px;background:var(--blue)}
.records-panel{left:0;top:2449px;width:1038px;height:354px;background:var(--navy)}
.records-list{left:165px;top:2478px;list-style:none}
.records-list li{display:flex;align-items:center;gap:12px;height:52.3px;font-size:14px;color:var(--white)}

/* cta */
.cta-bg{left:86px;top:2803px;width:1114px;height:419px;background:
  radial-gradient(ellipse 300px 150px at 800px 230px,rgba(230,190,190,.3),rgba(255,255,255,0)),
  linear-gradient(180deg,#ffffff,#f3f4f7 60%,#f7f2f2)}
.cta-bar{left:0;top:2803px;width:86px;height:328px;background:var(--blue)}
.cta-title{left:0;top:2905px;width:1200px;text-align:center;font-family:"Cinzel",serif;font-weight:500;font-size:29px;line-height:48px;color:var(--navy);letter-spacing:1px}

/* footer */
.footer{left:0;top:3222px;width:1200px;height:163px;background:var(--navy)}
.footer-brand{left:161px;top:3283px;display:flex;align-items:center;gap:14px}
.footer-brand .brand-mark{background:var(--white)}
.footer-brand .brand-name{color:var(--white);font-size:14px;line-height:16px}
.contact{position:absolute;display:flex;align-items:center;gap:12px;color:var(--white)}
.contact strong{display:block;font-size:13px;font-weight:600}
.contact span{font-size:13.5px}
.bottom-bar{left:0;top:3385px;width:1200px;height:62px;background:var(--blue)}
.copyright{left:163px;top:3407px;font-size:12.5px;color:var(--white)}
.social{left:942px;top:3410px;display:flex;gap:14px}
.social span{width:12px;height:12px;border-radius:50%;background:var(--white)}
</style>
</head>
<body>

<header class="hero">
  <div class="img-fill hero-photo" role="img" aria-label="Smiling man in a navy suit reaching out his hand for a handshake"></div>
  <div class="brand">
    <div class="brand-mark"></div>
    <div class="brand-name">BRIGHTFIELD<br>RECORD RELIEF</div>
  </div>
  <h1 class="hero-title"><span class="lead">CHANGE SO MUCH...</span><br>YOU'LL NEED TO<br>REINTRODUCE<br>YOURSELF</h1>
  <a class="btn" style="left:161px;top:381px;width:128px;height:40px" href="#contact">Contact Us</a>
</header>

<section>
  <div class="abs scales-bg" role="img" aria-label="Faint scales of justice and gavel"></div>
  <h2 class="section-title" style="left:0;top:598px;width:1200px;text-align:center">OUR SERVICES</h2>

  <div class="img-fill svc-photo svc-one" role="img" aria-label="Signing legal documents beside a judge's gavel"></div>
  <div class="svc-icon" style="left:478px;top:685px">
    <svg width="34" height="34" viewBox="0 0 34 34" fill="none" stroke="#fff" stroke-width="1.6"><rect x="6" y="4" width="18" height="25"/><line x1="10" y1="11" x2="20" y2="11"/><line x1="10" y1="16" x2="20" y2="16"/><line x1="10" y1="21" x2="16" y2="21"/><circle cx="25" cy="24" r="5"/></svg>
  </div>
  <div class="svc-label" style="left:210px;top:907px;width:338px">LEAVE YOUR PAST IN THE PAST</div>
  <div class="svc-arrow" style="left:548px;top:907px"><svg width="10" height="16" viewBox="0 0 10 16" fill="none" stroke="#fff" stroke-width="2"><polyline points="2,2 8,8 2,14"/></svg></div>

  <div class="img-fill svc-photo svc-two" role="img" aria-label="Lawyer with scales of justice and gavel explaining a document to a client"></div>
  <div class="svc-icon" style="left:940px;top:685px">
    <svg width="34" height="34" viewBox="0 0 34 34" fill="none" stroke="#fff" stroke-width="1.6"><rect x="5" y="5" width="20" height="24"/><path d="M15 11l5 2v4c0 3-2 5-5 6-3-1-5-3-5-6v-4z"/><line x1="28" y1="6" x2="28" y2="26"/></svg>
  </div>
  <div class="svc-label" style="left:672px;top:907px;width:338px">EXPUNGE YOUR CRIMINAL RECORDS</div>
  <div class="svc-arrow" style="left:1010px;top:907px"><svg width="10" height="16" viewBox="0 0 10 16" fill="none" stroke="#fff" stroke-width="2"><polyline points="2,2 8,8 2,14"/></svg></div>
</section>

<section>
  <div class="img-fill about-photo" role="img" aria-label="Team of five smiling legal professionals in business attire"></div>
  <div class="abs about-band"></div>
  <div class="abs about-panel"></div>
  <div class="abs about-strip"></div>
  <h2 class="panel-title" style="left:626px;top:1166px">ABOUT US</h2>
  <div class="abs about-text">
    <p>Lorem ipsum dolor sit amet, consectetuer adipiscing el sed diam nonummy nibh euismod tincidunt ut laoreet d magna aliquam erat volutpat.</p>
    <p>Ut wisi enim ad minim veniam, quis nostrud exe ullamcorper suscipit lobortis nisl ut aliquip ex ea commodo.</p>
  </div>
  <a class="btn" style="left:626px;top:1430px;width:128px;height:40px" href="#contact">Contact Us</a>
</section>

<section>
  <div class="abs benefits-bg" role="img" aria-label="Faint background of a consultation at an office desk"></div>
  <div class="abs benefits-bar"></div>
  <h2 class="section-title" style="left:160px;top:1640px">BENEFITS OF EXPUNGEMENT</h2>
  <p class="abs benefits-intro">Brightfield Record Relief is 5-star rated firm, which has been formed with the passing of the State Expungement Act of 2020. It is a subdivision of the Harlow Law Group, and since its creation has helped over 100 state residents successfully expunge their criminal records.</p>

  <div class="benefit" style="left:161px;top:1806px"><div class="benefit-icon"><svg width="34" height="34" viewBox="0 0 34 34" fill="none" stroke="#0b4b96" stroke-width="1.5"><rect x="5" y="9" width="24" height="15"/><circle cx="17" cy="16.5" r="4"/></svg></div><div class="benefit-text">More &amp; Better Job Opprtunities<br>Leading To Higher Income</div></div>
  <div class="benefit" style="left:490px;top:1806px"><div class="benefit-icon"><svg width="34" height="34" viewBox="0 0 34 34" fill="none" stroke="#0b4b96" stroke-width="1.5"><rect x="7" y="5" width="18" height="24"/><line x1="11" y1="11" x2="21" y2="11"/><line x1="11" y1="16" x2="21" y2="16"/><line x1="20" y1="22" x2="29" y2="29"/></svg></div><div class="benefit-text">Removing The Stigma Of<br>Having A Criminal Record</div></div>
  <div class="benefit" style="left:776px;top:1806px"><div class="benefit-icon"><svg width="34" height="34" viewBox="0 0 34 34" fill="none" stroke="#0b4b96" stroke-width="1.5"><path d="M11 6h12v8a6 6 0 0 1-12 0z"/><line x1="17" y1="20" x2="17" y2="26"/><line x1="11" y1="28" x2="23" y2="28"/></svg></div><div class="benefit-text">Qualifying For Government<br>Assistance Programs</div></div>

  <div class="benefit" style="left:161px;top:1889px"><div class="benefit-icon"><svg width="34" height="34" viewBox="0 0 34 34" fill="none" stroke="#0b4b96" stroke-width="1.5"><circle cx="19" cy="13" r="7"/><path d="M5 24h8l6 3 10-5"/></svg></div><div class="benefit-text">Loan Qualification &amp; Better<br>Loan Rates</div></div>
  <div class="benefit" style="left:490px;top:1889px"><div class="benefit-icon"><svg width="34" height="34" viewBox="0 0 34 34" fill="none" stroke="#0b4b96" stroke-width="1.5"><rect x="7" y="8" width="20" height="5"/><rect x="7" y="15" width="20" height="5"/><rect x="7" y="22" width="20" height="5"/></svg></div><div class="benefit-text">Better Education<br>Opportunities</div></div>
  <div class="benefit" style="left:776px;top:1889px"><div class="benefit-icon"><svg width="34" height="34" viewBox="0 0 34 34" fill="none" stroke="#0b4b96" stroke-width="1.5"><circle cx="17" cy="14" r="8"/><path d="M12 21l-3 8 8-4 8 4-3-8"/></svg></div><div class="benefit-text">Lower Insurance<br>Premiums</div></div>

  <div class="benefit" style="left:161px;top:1973px"><div class="benefit-icon"><svg width="34" height="34" viewBox="0 0 34 34" fill="none" stroke="#0b4b96" stroke-width="1.5"><rect x="6" y="8" width="18" height="20"/><circle cx="25" cy="9" r="5"/><line x1="10" y1="15" x2="20" y2="15"/><line x1="10" y1="20" x2="20" y2="20"/></svg></div><div class="benefit-text">Protecting Your<br>Privacy</div></div>
  <div class="benefit" style="left:490px;top:1973px"><div class="benefit-icon"><svg width="34" height="34" viewBox="0 0 34 34" fill="none" stroke="#0b4b96" stroke-width="1.5"><rect x="9" y="6" width="16" height="23"/><line x1="13" y1="11" x2="21" y2="11"/><line x1="13" y1="16" x2="21" y2="16"/><rect x="15" y="22" width="4" height="7"/></svg></div><div class="benefit-text">More Options For<br>Housing</div></div>

  <a class="btn" style="left:161px;top:2063px;width:130px;height:40px" href="#contact">Contact Us</a>
</section>

<section>
  <div class="img-fill records-photo" role="img" aria-label="Criminal background check form on a clipboard beside eyeglasses"></div>
  <div class="abs records-band"></div>
  <div class="abs records-panel"></div>
  <h2 class="panel-title" style="left:164px;top:2320px;line-height:45px">RECORDS ARE SEEN<br>BY PUBLIC</h2>
  <ul class="abs records-list">
    <li><svg width="20" height="20" viewBox="0 0 20 20" fill="none" stroke="#fff" stroke-width="2"><circle cx="10" cy="10" r="8"/><polyline points="6,10 9,13 17,4"/></svg>Public Reporting (www.statecourtrecords.org)</li>
    <li><svg width="20" height="20" viewBox="0 0 20 20" fill="none" stroke="#fff" stroke-width="2"><circle cx="10" cy="10" r="8"/><polyline points="6,10 9,13 17,4"/></svg>Police Reports</li>
    <li><svg width="20" height="20" viewBox="0 0 20 20" fill="none" stroke="#fff" stroke-width="2"><circle cx="10" cy="10" r="8"/><polyline points="6,10 9,13 17,4"/></svg>State Department Of Public Safety</li>
    <li><svg width="20" height="20" viewBox="0 0 20 20" fill="none" stroke="#fff" stroke-width="2"><circle cx="10" cy="10" r="8"/><polyline points="6,10 9,13 17,4"/></svg>District Attorney Prosecution Files</li>
    <li><svg width="20" height="20" viewBox="0 0 20 20" fill="none" stroke="#fff" stroke-width="2"><circle cx="10" cy="10" r="8"/><polyline points="6,10 9,13 17,4"/></svg>Court Records</li>
  </ul>
</section>

<section id="contact">
  <div class="abs cta-bg" role="img" aria-label="Faint background of a criminal record expungement form"></div>
  <div class="abs cta-bar"></div>
  <h2 class="abs cta-title">TO SEE IF YOU QUALIFY FOR EXPUNGEMENT OF FOR<br>ADDITIONAL INFORMATION CONTACT US</h2>
  <a class="btn" style="left:492px;top:3016px;width:215px;height:40px" href="#contact">Call Us : 555-010-4821</a>
</section>

<footer>
  <div class="abs footer"></div>
  <div class="abs footer-brand">
    <div class="brand-mark"></div>
    <div class="brand-name">BRIGHTFIELD<br>RECORD RELIEF</div>
  </div>
  <div class="contact" style="left:571px;top:3285px">
    <svg width="30" height="30" viewBox="0 0 30 30" fill="none" stroke="#fff" stroke-width="1.6"><path d="M8 4l4 5-2 3c1 3 4 6 7 7l3-2 5 4-3 4C13 25 5 17 4 8z"/></svg>
    <div><strong>Call Us</strong><span>555-010-4821</span></div>
  </div>
  <div class="contact" style="left:756px;top:3285px">
    <svg width="30" height="30" viewBox="0 0 30 30" fill="none" stroke="#fff" stroke-width="1.6"><rect x="3" y="8" width="24" height="17"/><polyline points="3,8 15,18 27,8"/></svg>
    <div><strong>Email Us</strong><span>info@brightfieldrelief.com</span></div>
  </div>
  <div class="abs bottom-bar"></div>
  <p class="abs copyright">© 2023 Brightfield Record Relief. All Rights Reserved.</p>
  <div class="abs social" aria-label="Social links"><span></span><span></span><span></span><span></span></div>
</footer>

</body>
</html>
```